6"x9" Postcard Mailer

A 6"x9" Postcard mailer targeted to forensic laboratories to advertise or mock forensic samples (https://veltrasync.example/products/mock-forensic-samples/).

Here is some copy, but we can modify if there is not enough space:

Headline:
Expedite Training, Validation, & R&D with Our Ready-to-Use Mock Samples

Bullet Points:

- Wide Variety of Sample Types: IRB-approved samples mimicking crime scene substances, including semen, hair, bone, saliva, blood, and vaginal epithelial cells.
- Diverse Scenarios: Simulate sexual assault and degraded samples for varied conditions.
- Custom Solutions: Tailored DNA quantities and concentrations to suit your lab's needs.

Use discount code PRAX47 for a 10% discount

```html
<!DOCTYPE html>
<html lang="en">
<head>
<meta charset="utf-8">
<title>Veltrasync Mock Samples – 6x9 Postcard Mailer</title>
<link href="https://fonts.googleapis.com/css2?family=Marcellus&family=Sorts+Mill+Goudy:ital@0;1&family=PT+Sans:ital,wght@0,400;0,700;1,400&family=Open+Sans:wght@400&display=swap" rel="stylesheet">
<style>
  :root {
    --board: #dcdde0;
    --brand-blue: #2357a6;
    --ink: #111111;
    --paper: #ffffff;
    --night: #000000;
    --trim-red: #e2262b;
    --bleed-navy: #2b3a78;
    --safe-green: #1aa54a;
  }
  * { box-sizing: border-box; margin: 0; padding: 0; }
  html, body { width: 1200px; height: 984px; overflow: hidden; background: var(--board); }
  .board { position: relative; width: 1200px; height: 984px; }

  .postcard {
    position: absolute; width: 549px; height: 371px; overflow: hidden;
    background: var(--paper);
  }
  .postcard svg.shape { position: absolute; inset: 0; width: 100%; height: 100%; }

  /* Front */
  .front .hero-photo {
    position: absolute; left: 0; top: 0; width: 549px; height: 287px;
    background:
      radial-gradient(ellipse 120px 90px at 20% 35%, #2f6fd6 0%, rgba(30,80,170,.6) 55%, transparent 100%),
      radial-gradient(ellipse 110px 90px at 52% 26%, #2a66cc 0%, rgba(30,80,170,.5) 55%, transparent 100%),
      radial-gradient(ellipse 170px 60px at 25% 88%, #eef0f4 0%, #c9ccd4 50%, transparent 100%),
      radial-gradient(ellipse 40px 18px at 68% 82%, #c21820 0%, transparent 100%),
      linear-gradient(90deg, #3a4150 0%, #141820 45%, #000 75%);
  }
  .contact { position: absolute; left: 409px; top: 22px; list-style: none;
    font: 400 9.6px/1 "Open Sans", sans-serif; color: var(--paper); }
  .contact li { display: flex; align-items: center; gap: 9px; height: 21px; }
  .contact svg { width: 14px; height: 14px; flex: none; }
  .headline { position: absolute; right: 18px; top: 209px; text-align: right;
    font: 400 29px/37px "Marcellus", serif; color: var(--paper); white-space: nowrap; letter-spacing: .3px; }
  .brand-name { position: absolute; left: 17px; top: 333px;
    font: 400 22px/1 "Marcellus", serif; color: var(--brand-blue); }

  /* Back */
  .back { background: var(--night); }
  .back .text-column { position: absolute; left: 0; top: 0; width: 200px; height: 371px; background: var(--paper); }
  .benefit { position: absolute; left: 19px; font: 400 12.6px/17px "Sorts Mill Goudy", serif; color: var(--ink); white-space: nowrap; }
  .benefit h3 { font: 400 12.6px/17px "Sorts Mill Goudy", serif; color: var(--brand-blue); }
  .divider { position: absolute; left: 43px; width: 132px; height: 1px; background: var(--brand-blue); }
  .offer { position: absolute; right: 91px; top: 22px; text-align: right; color: var(--paper);
    font-family: "PT Sans", sans-serif; white-space: nowrap; }
  .offer .line { font-size: 27px; line-height: 33px; }
  .offer .code { font-style: italic; margin-right: 8px; }
  .offer .percent { font-weight: 700; font-size: 44px; line-height: 48px; margin-top: 2px; }
  .offer .word { font-weight: 700; font-size: 26px; line-height: 28px; }
  .product-shot { position: absolute; left: 214px; top: 190px; width: 150px; height: 96px;
    background: radial-gradient(ellipse at 30% 55%, #5a86c8 0%, #1d3a6a 35%, transparent 60%),
                radial-gradient(ellipse at 75% 50%, #e8edf5 0%, #3a62a8 35%, transparent 62%); }

  /* Print guides */
  .guides { position: absolute; inset: 0; width: 100%; height: 100%; pointer-events: none; }
  .guides .trim { fill: none; stroke: var(--trim-red); stroke-width: 1.4; }
  .guides .bleed { fill: none; stroke: var(--bleed-navy); stroke-width: 2; }
  .guides .safe { fill: none; stroke: var(--safe-green); stroke-width: 2; stroke-dasharray: 5 4; }

  .caption { position: absolute; left: 0; width: 1200px; top: 918px; text-align: center;
    font: italic 400 27px/1 "PT Sans", sans-serif; color: var(--ink); }
</style>
</head>
<body>
<main class="board">

  <!-- Front, top row -->
  <section class="postcard front" style="left:26px;top:33px">
    <div class="hero-photo" role="img" aria-label="Photo of blue-gloved hands holding a swab over blood spatter on a white surface"></div>
    <svg class="shape" viewBox="0 0 549 371" preserveAspectRatio="none" aria-hidden="true">
      <path d="M549 192 L362 192 Q340 192 322 210 L165 352 Q143 371 93 371 L549 371 Z" fill="var(--brand-blue)"/>
    </svg>
    <ul class="contact">
      <li><svg viewBox="0 0 14 14"><circle cx="7" cy="7" r="7" fill="var(--brand-blue)"/><path d="M4.6 3.6l1.3 1.6-.7.9q.9 1.7 2.6 2.6l.9-.7 1.6 1.3-.8 1.2Q6.6 10.3 3.5 5.2Z" fill="#fff"/></svg>+1 555 014 7729</li>
      <li><svg viewBox="0 0 14 14"><circle cx="7" cy="7" r="7" fill="var(--brand-blue)"/><rect x="4" y="4.8" width="6" height="4.4" rx=".6" fill="#fff"/><path d="M4.2 5l2.8 2 2.8-2" fill="none" stroke="var(--brand-blue)" stroke-width=".7"/></svg>info@veltrasync.example</li>
    </ul>
    <h1 class="headline">Expedite Training,<br>Validation, and R&amp;D<br>with Our Ready-to-Use<br>MOCK SAMPLES</h1>
    <p class="brand-name">Veltrasync</p>
  </section>

  <!-- Back, top row -->
  <section class="postcard back" style="left:630px;top:33px">
    <div class="text-column"></div>
    <svg class="shape" viewBox="0 0 549 371" preserveAspectRatio="none" aria-hidden="true">
      <path d="M152 0 Q188 0 210 28 L340 165 Q368 189 408 189 L549 189 L549 0 Z" fill="var(--brand-blue)"/>
    </svg>
    <div class="benefit" style="top:27px"><h3>Wide Variety of Sample Types:</h3>IRB-approved samples<br>mimicking crime scene<br>substances, including semen,<br>hair, bone, saliva, blood, and<br>vaginal epithelial cells.</div>
    <div class="divider" style="top:146px"></div>
    <div class="benefit" style="top:162px"><h3>Diverse Scenarios:</h3>Simulate sexual assault and<br>degraded samples for varied<br>conditions.</div>
    <div class="divider" style="top:251px"></div>
    <div class="benefit" style="top:263px"><h3>Custom Solutions:</h3>Tailored DNA<br>quantities and concentrations to<br>suit your lab's needs.</div>
    <div class="offer">
      <p class="line">Use discount code</p>
      <p class="line"><span class="code">PRAX47</span>for a</p>
      <p class="percent">10%</p>
      <p class="word">DISCOUNT</p>
    </div>
    <div class="product-shot" role="img" aria-label="Photo of two mock sample kit boxes"></div>
  </section>

  <!-- Front, with guides -->
  <section class="postcard front" style="left:26px;top:522px">
    <div class="hero-photo" role="img" aria-label="Photo of blue-gloved hands holding a swab over blood spatter on a white surface"></div>
    <svg class="shape" viewBox="0 0 549 371" preserveAspectRatio="none" aria-hidden="true">
      <path d="M549 192 L362 192 Q340 192 322 210 L165 352 Q143 371 93 371 L549 371 Z" fill="var(--brand-blue)"/>
    </svg>
    <ul class="contact">
      <li><svg viewBox="0 0 14 14"><circle cx="7" cy="7" r="7" fill="var(--brand-blue)"/><path d="M4.6 3.6l1.3 1.6-.7.9q.9 1.7 2.6 2.6l.9-.7 1.6 1.3-.8 1.2Q6.6 10.3 3.5 5.2Z" fill="#fff"/></svg>+1 555 014 7729</li>
      <li><svg viewBox="0 0 14 14"><circle cx="7" cy="7" r="7" fill="var(--brand-blue)"/><rect x="4" y="4.8" width="6" height="4.4" rx=".6" fill="#fff"/><path d="M4.2 5l2.8 2 2.8-2" fill="none" stroke="var(--brand-blue)" stroke-width=".7"/></svg>info@veltrasync.example</li>
    </ul>
    <h1 class="headline">Expedite Training,<br>Validation, and R&amp;D<br>with Our Ready-to-Use<br>MOCK SAMPLES</h1>
    <p class="brand-name">Veltrasync</p>
    <svg class="guides" viewBox="0 0 549 371" preserveAspectRatio="none" aria-hidden="true">
      <rect class="trim" x=".7" y=".7" width="547.6" height="369.6"/>
      <rect class="bleed" x="6" y="7" width="537" height="357"/>
      <rect class="safe" x="10" y="10" width="529" height="350"/>
      <path class="safe" d="M82 10 V190 H175 V322 H303 V360"/>
    </svg>
  </section>

  <!-- Back, with guides -->
  <section class="postcard back" style="left:630px;top:522px">
    <div class="text-column"></div>
    <svg class="shape" viewBox="0 0 549 371" preserveAspectRatio="none" aria-hidden="true">
      <path d="M152 0 Q188 0 210 28 L340 165 Q368 189 408 189 L549 189 L549 0 Z" fill="var(--brand-blue)"/>
    </svg>
    <div class="benefit" style="top:27px"><h3>Wide Variety of Sample Types:</h3>IRB-approved samples<br>mimicking crime scene<br>substances, including semen,<br>hair, bone, saliva, blood, and<br>vaginal epithelial cells.</div>
    <div class="divider" style="top:146px"></div>
    <div class="benefit" style="top:162px"><h3>Diverse Scenarios:</h3>Simulate sexual assault and<br>degraded samples for varied<br>conditions.</div>
    <div class="divider" style="top:251px"></div>
    <div class="benefit" style="top:263px"><h3>Custom Solutions:</h3>Tailored DNA<br>quantities and concentrations to<br>suit your lab's needs.</div>
    <div class="offer">
      <p class="line">Use discount code</p>
      <p class="line"><span class="code">PRAX47</span>for a</p>
      <p class="percent">10%</p>
      <p class="word">DISCOUNT</p>
    </div>
    <div class="product-shot" role="img" aria-label="Photo of two mock sample kit boxes"></div>
    <svg class="guides" viewBox="0 0 549 371" preserveAspectRatio="none" aria-hidden="true">
      <path class="trim" d="M470 .7 H.7 V370.3 H251 V362"/>
      <path class="bleed" d="M6 7 H470 V193 H378 V326 H249 V365 H6 Z"/>
      <path class="safe" d="M10 10 H466 V188 H374 V321 H245 V360 H10 Z"/>
    </svg>
  </section>

  <p class="caption">with Bleed, Trim and Safe areas</p>
</main>
</body>
</html>
```